Tidewalk Intro Course QM Dive Bonaire

QM Dive is looking for a great flyer to promote our Tidewalk Intro Course around Bonaire, the Caribbean.

Bonaire is shore dive capital of the world.
Our guests rent a pick-up truck. we would like to inform them about the possibilities of the Tidewalk Intro Dive.

We have the logo, images and text available. Its the catchy and mind blowing design we are looking for to create an eye-catch flyer.
One side will be in English, the other side will be in Dutch.

Target Market(s)

Visitors (non divers) of the island Bonaire

Industry/Entity Type

Diving industry

Font styles to use
Sans Serif

Colors
0094D4
00A9DD
6FCCEA
C7EBF8
E9F6FB
F0912C
F2A743
F7CA91
FBE8D2
FDF5EE

Requirements
Must have
• The picture with the car and divers next to it is mandatory. Inspire to go for a tidewalk intro dive, show the beauty under water, easy to come dive with us, just takes half a day
Should not have
• Should not have pictures taken not around Bonaire.

```html
<!DOCTYPE html>
<html lang="en">
<head>
<meta charset="utf-8">
<title>Tidewalk Intro Course on Bonaire – Flyer</title>
<link rel="stylesheet" href="https://fonts.googleapis.com/css2?family=Montserrat:ital,wght@0,400;0,600;0,700;0,800;1,700&display=swap">
<style>
  :root {
    --page-bg: #e9eaeb;
    --sea-top: #8fd6f1;
    --sea-mid: #2f9fdc;
    --sea-deep: #0b72b3;
    --title-accent: #0a68b8;
    --heading-blue: #0f6fc4;
    --body-blue: #1d6db5;
    --alert-red: #e3222b;
    --ring-blue: #1679c4;
    --white: #ffffff;
    --brand-dark: #1b1b1b;
  }
  * { margin: 0; padding: 0; box-sizing: border-box; }
  html, body { width: 1200px; height: 1200px; overflow: hidden; }
  body {
    background: var(--page-bg);
    font-family: "Montserrat", Arial, sans-serif;
    position: relative;
  }
  .flyer {
    position: absolute;
    left: 217px; top: 60px;
    width: 764px; height: 1080px;
    overflow: hidden;
    background: linear-gradient(180deg, var(--sea-top) 0%, var(--sea-mid) 30%, var(--sea-deep) 72%, var(--sea-deep) 100%);
  }
  .reef-band {
    position: absolute; left: 0; top: 660px; width: 764px; height: 250px;
    background: linear-gradient(180deg, rgba(255,255,255,0) 0%, rgba(255,255,255,0.4) 50%, #ffffff 95%);
  }
  .footer-panel {
    position: absolute; left: 0; top: 900px; width: 764px; height: 180px;
    background: var(--white);
  }
  .title {
    position: absolute; left: 36px; top: 12px; z-index: 2;
    color: var(--white);
    font-weight: 700; font-size: 62px; line-height: 70px; letter-spacing: -1.5px;
  }
  .title .place { color: var(--title-accent); }
  .brand-tab {
    position: absolute; left: 557px; top: 0; width: 171px; height: 225px;
    background: var(--white);
    border-radius: 0 0 86px 86px;
    display: flex; flex-direction: column; align-items: center; justify-content: center;
    padding-top: 26px; gap: 12px;
  }
  .brand-tab .brand-dot { width: 70px; height: 70px; border-radius: 50%; background: var(--title-accent); }
  .brand-tab .brand-name { font-weight: 800; font-size: 20px; color: var(--brand-dark); letter-spacing: 0.5px; }
  .intro {
    position: absolute; left: 36px; top: 236px; width: 710px; z-index: 3;
    color: var(--white); font-weight: 400; font-size: 18px; line-height: 23px;
  }
  .photo {
    position: absolute; border-radius: 50%;
    border: 6px solid var(--ring-blue);
    z-index: 1;
  }
  .photo--reef { left: 121px; top: 269px; width: 258px; height: 258px;
    background: radial-gradient(circle at 55% 35%, #5d7fa8 0%, #48648c 35%, #8a8f98 70%, #b9b6ad 100%); }
  .photo--beach { left: 25px; top: 461px; width: 168px; height: 168px;
    background: linear-gradient(180deg, #8fc6e6 0%, #39a6c9 35%, #e9e6df 60%, #d8d3c8 100%); }
  .photo--gear { left: 208px; top: 527px; width: 155px; height: 155px;
    background: linear-gradient(180deg, #c9dfe6 0%, #a9c3c9 35%, #4a4a48 60%, #6e655b 100%); }
  .perks {
    position: absolute; left: 398px; top: 348px; width: 362px; z-index: 2;
    color: var(--white);
  }
  .perks h2 {
    margin-left: 48px; height: 24px;
    color: var(--heading-blue); font-weight: 700; font-size: 16px; line-height: 22px;
    margin-bottom: 1px;
  }
  .perk {
    display: flex; align-items: center; gap: 16px;
    height: 47px;
    font-size: 12.6px; line-height: 15.5px; font-weight: 400;
  }
  .perk svg { flex: 0 0 32px; width: 32px; height: 32px; }
  .details {
    position: absolute; left: 36px; top: 930px; width: 700px; z-index: 2;
  }
  .details h3 { color: var(--alert-red); font-weight: 700; font-size: 15px; line-height: 20px; margin-bottom: 4px; }
  .details p { color: var(--body-blue); font-size: 12.2px; line-height: 15.5px; }
  .details .cta {
    margin-top: 10px; color: var(--alert-red);
    font-weight: 700; font-style: italic; font-size: 16.4px; line-height: 23.5px; letter-spacing: -0.4px;
  }
</style>
</head>
<body>
<main class="flyer">
  <div class="reef-band" role="img" aria-label="White silhouettes of coral, fish and a swimming diver along the sea floor"></div>
  <div class="footer-panel"></div>

  <h1 class="title">Tidewalk<br>Intro Course<br>on <span class="place">Bonaire</span></h1>

  <div class="brand-tab">
    <div class="brand-dot"></div>
    <div class="brand-name">REEFMARK</div>
  </div>

  <div class="photo photo--reef" role="img" aria-label="Underwater reef with sea fans and a school of blue fish"></div>
  <div class="photo photo--beach" role="img" aria-label="Two divers in wetsuits on the beach next to a white pick-up truck"></div>
  <div class="photo photo--gear" role="img" aria-label="Dive tanks and regulators resting on rocks by the shore"></div>

  <p class="intro">Fall in love with diving in our underwater paradise. Under the guidance<br>of a dive instructor you will learn the basic skills for peaceful diving in a fun<br>and easy way.</p>

  <section class="perks">
    <h2>Develop a passion for marine life</h2>
    <div class="perk">
      <svg viewBox="0 0 34 34" fill="#fff"><circle cx="17" cy="5" r="4"/><rect x="4" y="11" width="26" height="4" rx="2"/><rect x="13" y="11" width="8" height="12"/><rect x="13" y="21" width="3.4" height="12" rx="1.5"/><rect x="17.6" y="21" width="3.4" height="12" rx="1.5"/></svg>
      <span>Ages 10 and up can sign up for our tidewalk intro dive</span>
    </div>
    <div class="perk">
      <svg viewBox="0 0 34 34" fill="none" stroke="#fff" stroke-width="2.5"><path d="M3 8 Q10 5 17 9 Q24 5 31 8 V27 Q24 24 17 28 Q10 24 3 27 Z"/><path d="M17 9 V28"/></svg>
      <span>You'll dive straight into the water after a brief<br>theoretic introduction</span>
    </div>
    <div class="perk">
      <svg viewBox="0 0 34 34"><circle cx="17" cy="17" r="15" fill="#fff"/><path d="M17 8 V17 H24" stroke="#1679c4" stroke-width="2.5" fill="none"/></svg>
      <span>The Tidewalk Intro Course will<br>take 3-4 hours</span>
    </div>
    <div class="perk">
      <svg viewBox="0 0 34 34" fill="none" stroke="#fff" stroke-width="3"><path d="M4 10 V30 H26"/><path d="M8 16 L15 23 L31 5"/></svg>
      <span>Before participating, you are required to fill out<br>a medical questionnaire</span>
    </div>
    <div class="perk">
      <svg viewBox="0 0 34 34" fill="#fff"><circle cx="17" cy="9" r="5"/><circle cx="7" cy="12" r="4"/><circle cx="27" cy="12" r="4"/><path d="M9 30 Q9 17 17 17 Q25 17 25 30 Z"/><path d="M1 28 Q1 18 7 18 Q10 18 11 20 Q8 23 8 28 Z"/><path d="M33 28 Q33 18 27 18 Q24 18 23 20 Q26 23 26 28 Z"/></svg>
      <span>A group consists of a maximum of 4 people</span>
    </div>
    <div class="perk">
      <svg viewBox="0 0 34 34" fill="none" stroke="#fff" stroke-width="3"><path d="M3 22 Q8 16 13 22 T23 22 T33 20"/><path d="M5 29 Q10 24 15 29 T25 29"/><path d="M14 17 Q10 6 20 4 Q30 4 29 13 Q28 19 22 18"/></svg>
      <span>Experience the splendor of the ocean without<br>much distraction by other divers</span>
    </div>
    <div class="perk">
      <svg viewBox="0 0 34 34" fill="none" stroke="#fff" stroke-width="2.2"><path d="M9 6 H25 L32 13 L17 30 L2 13 Z"/><path d="M2 13 H32 M12 6 L10 13 L17 30 L24 13 L22 6"/></svg>
      <span>And enjoy a lot of personal attention given<br>by your instructor</span>
    </div>
  </section>

  <section class="details">
    <h3>Underwater paradise</h3>
    <p>Bonaire is the place to learn how to scuba dive. After a brief introduction we will directly dive into the sea,<br>where the reef starts in shallow waters. We know the perfect dive sites for beginners. Here, the sea bed slopes<br>gradually down and you'll be amazed by the most beautiful fish and corals.</p>
    <p class="cta">Stop by at our Front office and we are happy to answer all your questions or to book<br>your 'Tidewalk Intro Dive'!</p>
  </section>
</main>
</body>
</html>
```